Business card design needed for Pollen Bakes

We need a new business card designed for our business. We create complete DIY cake kits to be delivered Australia Wide.

I would like our logo used (see attached).

Industry/Entity Type

Business

Contact Information for Business Card

Pollen Bakes - Complete DIY Cake Kits
www.pollenbakes.com.au
0472 315 904
sales@pollenbakes.com.au
www.facebook.com/pollenbakes1

Requirements
Must have
• logo

```html
<!DOCTYPE html>
<html lang="en">
<head>
<meta charset="utf-8">
<title>Pollen Bakes – Business Card</title>
<link rel="stylesheet" href="https://fonts.googleapis.com/css2?family=Arimo:wght@400;700&display=swap">
<style>
  :root {
    --teal: #7fc6c0;
    --chocolate: #6b4330;
    --chocolate-light: #8a5a40;
    --paper: #ffffff;
    --text-light: #ffffff;
    --brand-red: #c0272d;
    --art-pink: #f4b6cf;
    --art-cream: #f7e7c9;
  }
  html, body {
    margin: 0;
    padding: 0;
    width: 1200px;
    height: 653px;
    overflow: hidden;
    background: var(--paper);
  }
  .card {
    position: relative;
    width: 1200px;
    height: 653px;
    overflow: hidden;
    font-family: "Arimo", Arial, sans-serif;
  }
  .card-backdrop {
    position: absolute;
    inset: 0;
    width: 1200px;
    height: 653px;
  }
  .brand-artwork {
    position: absolute;
    left: 70px;
    top: 95px;
    width: 350px;
    height: 300px;
    border-radius: 50%;
    background: radial-gradient(ellipse at 50% 40%, var(--art-pink) 0%, var(--art-cream) 55%, rgba(247,231,201,0) 72%);
  }
  .brand-name {
    position: absolute;
    left: 60px;
    top: 405px;
    width: 400px;
    margin: 0;
    font-size: 60px;
    font-weight: 700;
    line-height: 1.1;
    color: var(--brand-red);
  }
  .contact-block {
    position: absolute;
    left: 655px;
    top: 279px;
    width: 520px;
    color: var(--text-light);
  }
  .contact-name {
    margin: 0;
    font-size: 50px;
    font-weight: 400;
    line-height: 55px;
    white-space: nowrap;
  }
  .contact-role {
    margin: 0;
    font-size: 28px;
    line-height: 34px;
  }
  .contact-lines {
    list-style: none;
    margin: 78px 0 0;
    padding: 0;
    font-size: 28px;
    line-height: 36.7px;
    white-space: nowrap;
  }
</style>
</head>
<body>
  <div class="card">
    <svg class="card-backdrop" viewBox="0 0 1200 653" aria-hidden="true">
      <rect width="1200" height="653" fill="var(--teal)"/>
      <circle cx="-130" cy="326" r="735" fill="var(--chocolate)"/>
      <circle cx="-130" cy="326" r="722" fill="none" stroke="var(--chocolate-light)" stroke-width="4"/>
      <circle cx="-150" cy="326" r="700" fill="var(--paper)"/>
    </svg>

    <div class="brand-artwork" role="img" aria-label="Illustration of a baker piping pink icing onto a cupcake"></div>
    <p class="brand-name">Pollen Bakes</p>

    <div class="contact-block">
      <h1 class="contact-name">Mirren Calloway</h1>
      <p class="contact-role">Manager</p>
      <ul class="contact-lines">
        <li>0472 315 904</li>
        <li>www.pollenbakes.com.au</li>
        <li>sales@pollenbakes.com.au</li>
        <li>www.facebook.com/pollenbakes1</li>
      </ul>
    </div>
  </div>
</body>
</html>
```